Business Card Design Project

- makeup artist business card

- original and creative

- Elegant design

- Feel free to come out with cool designs but stick to being elegant and attractive

- Design relates to makeup

- includes name, occupation, contact numbers, email, website

- regular size business card

- round corner card

- double sided

- on 1 side it should just have the website name in the center " browsandblush.example "

Industry/Entity Type

Business

Requirements
Must have
• Marla Voss
Makeup Artist
USA: +1 (415)872-6410
Singapore: +65 83027715
marlavoss@browsandblush.example
www.browsandblush.example
Should not have
• nothing cartoon looking.
Pictures of makeup being grab from the internet.. Examples: eyes or lips.

```html
<!DOCTYPE html>
<html lang="en">
<head>
<meta charset="utf-8">
<title>Marla Voss – Makeup Artist Business Card</title>
<link href="https://fonts.googleapis.com/css2?family=Cinzel:wght@400;500&display=swap" rel="stylesheet">
<style>
  :root {
    --page-bg: #ffffff;
    --card-bg: #050505;
    --card-edge: #111111;
    --ink-tan: #b48c69;
    --ink-tan-soft: #a8825f;
    --portrait-warm: #3a1f18;
    --portrait-mid: #1b0f0c;
    --shadow: rgba(0, 0, 0, 0.45);
  }
  * { margin: 0; padding: 0; box-sizing: border-box; }
  html, body {
    width: 1200px;
    height: 900px;
    overflow: hidden;
    background: var(--page-bg);
  }
  .canvas {
    position: relative;
    width: 1200px;
    height: 900px;
  }
  .card {
    position: absolute;
    top: 306px;
    width: 506px;
    height: 288px;
    border-radius: 28px;
    background: var(--card-bg);
    overflow: hidden;
    box-shadow: 4px 10px 14px var(--shadow);
  }
  .card--front { left: 84px; }
  .card--back  { left: 612px; }

  .front-text {
    position: absolute;
    left: 0;
    width: 100%;
    text-align: center;
    font-family: "Cinzel", "Times New Roman", serif;
    color: var(--ink-tan);
    letter-spacing: 0.08em;
  }
  .identity { top: 110px; }
  .identity__name,
  .identity__role {
    font-size: 19px;
    line-height: 26px;
    font-weight: 500;
  }
  .contact { top: 194px; }
  .contact__line {
    font-size: 14px;
    line-height: 22px;
    color: var(--ink-tan-soft);
  }

  .portrait-area {
    position: absolute;
    left: 0;
    top: 0;
    width: 210px;
    height: 100%;
    background:
      radial-gradient(ellipse 90px 120px at 95px 120px, var(--portrait-warm) 0%, var(--portrait-mid) 60%, transparent 100%),
      linear-gradient(90deg, var(--portrait-mid) 0%, var(--card-bg) 100%);
  }
  .website {
    position: absolute;
    left: 152px;
    top: 132px;
    width: 340px;
    text-align: center;
    font-family: "Cinzel", "Times New Roman", serif;
    font-size: 15px;
    letter-spacing: 0.08em;
    color: var(--ink-tan);
  }
</style>
</head>
<body>
  <main class="canvas">
    <section class="card card--front" aria-label="Card front">
      <div class="front-text identity">
        <p class="identity__name">Marla Voss</p>
        <p class="identity__role">Makeup Artist</p>
      </div>
      <div class="front-text contact">
        <p class="contact__line">USA: +1 (415)872-6410</p>
        <p class="contact__line">Singapore: +65 83027715</p>
        <p class="contact__line">marlavoss@browsandblush.example</p>
      </div>
    </section>

    <section class="card card--back" aria-label="Card back">
      <div class="portrait-area" role="img" aria-label="Portrait photograph of the makeup artist with auburn hair, fading into black"></div>
      <p class="website">www.BrowsAndBlush.example</p>
    </section>
  </main>
</body>
</html>
```